Birch & Ember Website Design (Rustic/Western)

OVERVIEW
Birch & Ember Supply House (aka Birch & Ember) manufactures rustic / western furniture and décor for cabins, lodges, and ranches. We also offer a line of accessories to complement our product line.
WEB PAGE (www.BirchAndEmber.example)
We are looking for a new web page design to represent our mountain-style (log furniture) and country-style (barnwood furniture) product line. We would like to re-create our existing homepage with a similar style template for our product line.
Our website is currently under construction – a draft has been published as an example outline. We are currently using Plinkora.example for our online store.
THEME
The overall theme needs to appear rustic, yet elegant. Listed below are only suggestions, not requirements. Please use your own creativity.
* Photographs: We will use our own photographs, for now any photograph will suffice.
* Background Colors: dark brown (rgb 21-9-2), medium brown (rgb 39-17-4), light brown (rgb 72-34-3). White background is also an option.
* Font Colors: beige (rgb 233-164-118), gold (rgb 151-98-2)
• Mountain-Style Images: cabin, wildlife, mountains, fishing, wildlife, trees, etc.
* Mountain-Style Colors: hunter green
* Country-Style Images: western, ranch, barn, farm animals, horse buggies, horseshoes, etc.
* Country-Style Colors: maroon
Thanks to all who are participating.
Target Market(s)
Outdoor enthusiasts who enjoy mountain living or country living. Our primary target market is our local market and within a 100 mile radius of our location.
Industry/Entity Type
Construction
Requirements
Must have
- Rustic, yet elegant design.
Homepage and product template page for displaying each item.
Nice to have
- Source code and functionality is optional.
Mountain-Style theme to represent our collection of log furniture and décor suited for cabins and lodges. Suggested color: hunter green. Images may include cabin, wildlife, mountains, fishing, wildlife, trees, etc.
Country-Style theme to represent our collection of barnwood furniture and décor suited for farms and ranches. Suggested color: maroon. Images may include western, ranch, barn, farm animals, horse buggies, horseshoes, etc.

```html
<!DOCTYPE html>
<html lang="en">
<head>
<meta charset="utf-8">
<title>Birch &amp; Ember Supply House</title>
<link rel="stylesheet" href="https://fonts.googleapis.com/css2?family=Oswald:wght@300;400&family=Questrial&display=swap">
<style>
  :root {
    --wood-light: #b57a40;
    --wood-mid: #9a5f2a;
    --wood-dark: #7a4618;
    --band: rgba(40, 18, 4, 0.45);
    --panel: rgba(60, 30, 8, 0.45);
    --ink-dark: #2a1405;
    --ink-white: #ffffff;
    --beige: #e9a476;
    --gold: #c98a3a;
    --card-bg: #1a0c03;
    --card-edge: #5a3312;
    --footer-bg: #150902;
    --footer-edge: #3f220b;
    --photo-hero: #857463;
    --photo-mountain: #9a6b45;
    --photo-country: #8c9184;
    --dot: #b9b0a8;
  }
  * { margin: 0; padding: 0; box-sizing: border-box; }
  html, body { width: 1200px; height: 994px; overflow: hidden; }
  body { font-family: "Questrial", "Century Gothic", sans-serif; }

  .page { position: relative; width: 1200px; height: 994px; overflow: hidden; }
  .wood-backdrop {
    position: absolute; inset: 0;
    background: linear-gradient(90deg, var(--wood-dark) 0%, var(--wood-light) 18%, var(--wood-mid) 36%, var(--wood-light) 52%, var(--wood-mid) 70%, var(--wood-light) 86%, var(--wood-dark) 100%);
  }

  .topbar { position: absolute; left: 0; top: 0; width: 1200px; height: 95px; background: var(--band); }
  .nav { position: absolute; top: 72px; left: 0; width: 1200px; list-style: none; }
  .nav li { position: absolute; font-size: 11px; color: var(--ink-white); white-space: nowrap; letter-spacing: 0.2px; }
  .nav .has-menu::after {
    content: ""; position: absolute; left: 50%; top: 16px; margin-left: -4px;
    border-left: 4px solid transparent; border-right: 4px solid transparent; border-top: 5px solid var(--ink-white);
  }

  .hero { position: absolute; left: 186px; top: 112px; width: 840px; height: 395px; background: var(--panel); }
  .brand-box {
    position: absolute; left: 94px; top: 15px; width: 109px; height: 68px;
    background: var(--card-bg); display: flex; align-items: center; justify-content: center;
    color: var(--beige); font-size: 14px; text-align: center;
  }
  .hero-photo { position: absolute; left: 211px; top: 15px; width: 523px; height: 345px; background: var(--photo-hero); }
  .dots { position: absolute; left: 0; top: 370px; width: 840px; display: flex; justify-content: center; gap: 3px; padding-left: 88px; }
  .dots span { width: 8px; height: 8px; border-radius: 50%; background: var(--dot); }
  .dots .active { background: var(--ink-white); }

  .intro-title {
    position: absolute; left: 0; top: 530px; width: 1212px; text-align: center;
    font-family: "Oswald", "Arial Narrow", sans-serif; font-weight: 400; font-size: 44px;
    color: var(--ink-white); letter-spacing: 1px; line-height: 1;
  }
  .intro-text { position: absolute; left: 186px; top: 592px; width: 840px; color: var(--ink-dark); font-size: 12.5px; line-height: 15px; letter-spacing: 0.35px; }
  .intro-text p + p { margin-top: 15px; }

  .collection {
    position: absolute; top: 756px; width: 429px; height: 125px;
    background: var(--card-bg); border: 3px solid var(--card-edge);
  }
  .collection-photo { position: absolute; left: 6px; top: 5px; width: 134px; height: 109px; border: 3px solid var(--card-edge); }
  .photo-mountain { background: var(--photo-mountain); }
  .photo-country { background: var(--photo-country); }
  .collection-name {
    position: absolute; left: 163px; top: 26px; color: var(--beige);
    font-family: "Oswald", "Arial Narrow", sans-serif; font-weight: 400; font-size: 32px; line-height: 1; letter-spacing: 0.3px;
  }
  .collection-sub { position: absolute; left: 165px; top: 68px; color: var(--beige); font-size: 21px; letter-spacing: 8px; line-height: 1; }

  .footer { position: absolute; left: 0; top: 906px; width: 1200px; height: 88px; background: var(--footer-bg); border-top: 3px solid var(--footer-edge); }
  .contact-title { position: absolute; left: 302px; top: 12px; font-size: 12px; color: var(--gold); }
  .contact-line { position: absolute; left: 294px; display: flex; align-items: center; gap: 9px; font-size: 12px; color: var(--beige); }
  .contact-phone { top: 35px; left: 306px; }
  .contact-mail { top: 58px; }
  .social { position: absolute; left: 718px; top: 12px; display: flex; gap: 9px; align-items: center; }
  .social .dot-link { width: 30px; height: 30px; border-radius: 50%; background: var(--gold); }
  .social .handle { font-size: 11px; color: var(--gold); margin-left: 5px; }
  .copyright { position: absolute; left: 718px; top: 52px; font-size: 10px; line-height: 13px; color: var(--gold); }
</style>
</head>
<body>
<div class="page">
  <div class="wood-backdrop" role="img" aria-label="Background of vertical wooden planks in warm brown tones"></div>

  <header class="topbar">
    <ul class="nav">
      <li style="left:306px">HOME</li>
      <li class="has-menu" style="left:369px">SPACES</li>
      <li style="left:442px">ONLINE STORE</li>
      <li style="left:548px">BARGAIN CORNER</li>
      <li style="left:676px">ABOUT US</li>
      <li style="left:759px">CONTACT US</li>
      <li style="left:859px">Cart (0)</li>
    </ul>
  </header>

  <section class="hero">
    <div class="brand-box">Birch &amp; Ember</div>
    <div class="hero-photo" role="img" aria-label="Photo of rustic barnwood planter boxes with red flowers"></div>
    <div class="dots"><span></span><span></span><span></span><span></span><span></span><span></span><span class="active"></span><span></span></div>
  </section>

  <h1 class="intro-title">LOREM IPSUM</h1>
  <div class="intro-text">
    <p>dolor sit amet, consectetur adipiscing elit. Sed molestie neque eget lectus pulvinar euismod. Nulla sed magna elit, at lacinia tortor. Nullam elit velit, tristique eget blandit eget, pulvinar in velit. Nam vehicula magna ornare orci ultricies luctus. Praesent in libero risus. Aenean sit amet nisi arcu, cursus blandit odio. Nulla</p>
    <p>dignissim tincidunt neque vel posuere. Integer vulputate vestibulum dolor vel tincidunt. Sed elementum lacinia ante eu varius. Suspendisse nec mi a est ultrices pharetra consequat vitae elit. Fusce sed rutrum leo. Sed adipiscing condimentum varius. Donec faucibus auctor fringilla. Ut sollicitudin odio at ipsum tincidunt sed pellentesque dui eleifend. Nullam id congue arcu. Vivamus enim justo, pretium ultrices ultrices et, sollicitudin id massa.</p>
  </div>

  <a class="collection" style="left:174px">
    <div class="collection-photo photo-mountain" role="img" aria-label="Photo of a mountain landscape in autumn"></div>
    <div class="collection-name">MOUNTAIN-STYLE</div>
    <div class="collection-sub">COLLECTION</div>
  </a>
  <a class="collection" style="left:624px">
    <div class="collection-photo photo-country" role="img" aria-label="Photo of a ranch scene with farm animals"></div>
    <div class="collection-name">MOUNTAIN-STYLE</div>
    <div class="collection-sub">COLLECTION</div>
  </a>

  <footer class="footer">
    <div class="contact-title">CONTACT US</div>
    <div class="contact-line contact-phone">
      <svg width="18" height="18" viewBox="0 0 18 18" aria-hidden="true"><rect width="18" height="18" rx="3" fill="var(--gold)"/><path d="M6 4 L8 4 L8.8 6.8 L7.6 7.8 C8.2 9.2 9 10 10.3 10.6 L11.3 9.4 L14 10.2 L14 12.2 C14 13 13.3 13.6 12.4 13.5 C8 13 5 10 4.5 5.6 C4.4 4.7 5 4 6 4 Z" fill="var(--footer-bg)"/></svg>
      <span>000 0000 00000</span>
    </div>
    <div class="contact-line contact-mail">
      <svg width="28" height="18" viewBox="0 0 28 18" aria-hidden="true"><rect x="1" y="1" width="26" height="16" fill="none" stroke="var(--gold)" stroke-width="1.5"/><path d="M1 1 L14 10 L27 1" fill="none" stroke="var(--gold)" stroke-width="1.5"/></svg>
      <span>info@birchandember.example</span>
    </div>
    <div class="social" aria-label="Social links">
      <span class="dot-link"></span><span class="dot-link"></span><span class="dot-link"></span>
      <span class="handle">birchnember sh</span>
    </div>
    <div class="copyright">© 2014 Copyright Birch &amp; Ember Supply House<br>All Rights Reserved.</div>
  </footer>
</div>
</body>
</html>
```